Business card design needed

Double sided
Color, unique, elegant

Maybe put this quote somewhere?? But I think it might make it to cluttered?
“The Pilates Method of Body
Conditioning develops the body
uniformly, corrects posture, restores
vitality, invigorates the mind and
elevates the spirit”
- Henrik Dovacombe

Industry/Entity Type

Business

Contact Information for Business Card

Marta Kellbrook
Pilates Instructor & Personal trainer
Mobile: 0498265043
www.lorvix.com.au
email: lorvixhealth.fitness@qentamail.com

```html
<!DOCTYPE html>
<html lang="en">
<head>
<meta charset="utf-8">
<title>Lorvix Health and Fitness – Business Card</title>
<link rel="stylesheet" href="https://fonts.googleapis.com/css2?family=Tinos:ital,wght@0,400;0,700;1,400&display=swap">
<style>
  :root {
    --page: #ecebe8;
    --card-black: #07040c;
    --violet-deep: #2a0f4a;
    --violet: #6b2fb0;
    --violet-glow: #a25be0;
    --magenta: #c24fb6;
    --edge-green: #7cd27a;
    --edge-pink: #d77acb;
    --text-white: #f4f1f6;
    --accent-green: #8fd88a;
    --brand-pink: #dca0d8;
  }
  * { box-sizing: border-box; margin: 0; padding: 0; }
  html, body { width: 1200px; height: 740px; overflow: hidden; }
  body {
    background: var(--page);
    font-family: "Tinos", "Times New Roman", serif;
    display: flex;
    align-items: center;
    justify-content: center;
    gap: 44px;
  }
  .card {
    position: relative;
    width: 540px;
    height: 316px;
    background: var(--card-black);
    border-top: 5px solid var(--edge-green);
    border-left: 5px solid var(--edge-green);
    border-bottom: 5px solid var(--edge-pink);
    border-right: 5px solid var(--edge-pink);
    overflow: hidden;
    box-shadow: 0 8px 22px rgba(0,0,0,.22);
  }
  .card__texture {
    position: absolute;
    inset: 0;
    background:
      radial-gradient(ellipse 55% 38% at 52% 50%, rgba(162,91,224,.75), rgba(107,47,176,.35) 55%, transparent 80%),
      radial-gradient(ellipse 30% 20% at 60% 48%, rgba(194,79,182,.45), transparent 75%),
      linear-gradient(180deg, var(--card-black), var(--violet-deep) 50%, var(--card-black));
  }
  /* Front */
  .contact {
    position: absolute;
    left: 34px;
    top: 138px;
    color: var(--text-white);
  }
  .contact__name { font-size: 25px; font-weight: 400; letter-spacing: .5px; }
  .contact__role { font-size: 16px; color: var(--accent-green); margin-top: 2px; }
  .contact__list {
    list-style: none;
    margin: 8px 0 0 150px;
    font-size: 14px;
    line-height: 1.5;
  }
  .contact__list b { font-weight: 400; color: var(--accent-green); margin-right: 6px; }
  /* Back */
  .quote {
    position: absolute;
    right: 26px;
    top: 26px;
    width: 270px;
    text-align: center;
    color: var(--text-white);
    font-size: 15px;
    line-height: 1.45;
  }
  .quote__author { display: block; color: var(--accent-green); margin-top: 2px; }
  .brand {
    position: absolute;
    left: 48px;
    bottom: 40px;
    display: flex;
    align-items: center;
    gap: 14px;
    color: var(--brand-pink);
  }
  .brand__dot {
    width: 30px; height: 30px;
    border-radius: 50%;
    background: var(--accent-green);
  }
  .brand__name { font-size: 58px; font-weight: 400; letter-spacing: 3px; line-height: 1; }
  .brand__tagline {
    position: absolute;
    left: 92px;
    bottom: 18px;
    color: var(--brand-pink);
    font-size: 19px;
  }
</style>
</head>
<body>
  <section class="card card--front">
    <div class="card__texture" role="img" aria-label="Purple woven light-streak texture on black"></div>
    <div class="contact">
      <h1 class="contact__name">Marta Kellbrook</h1>
      <p class="contact__role">Pilates Instructor &amp; Personal trainer</p>
      <ul class="contact__list">
        <li><b>M:</b>0498265043</li>
        <li><b>W:</b>www.lorvix.com.au</li>
        <li><b>E:</b>lorvixhealth.fitness@qentamail.com</li>
      </ul>
    </div>
  </section>

  <section class="card card--back">
    <div class="card__texture" role="img" aria-label="Purple woven light-streak texture on black"></div>
    <blockquote class="quote">
      “The Pilates Method of Body Conditioning develops the body uniformly, corrects posture, restores vitality, invigorates the mind and elevates the spirit”
      <span class="quote__author">- Henrik Dovacombe</span>
    </blockquote>
    <div class="brand">
      <span class="brand__dot"></span>
      <span class="brand__name">LORVIX</span>
    </div>
    <p class="brand__tagline">Health and Fitness</p>
  </section>
</body>
</html>
```